Swim school needs flyer design

Need revamp of flyer design. Attached last years flyer (BCP A4 Holiday Leaflet-v6.2 (1)). Also attached is this years information in word format (BCP A4 BCP & Holiday Leaflet 2014-2015).
This flyer must fit with our logo (Blue Current Pools-RGB). This flyer is our first point of call for many of our clients. With the amount of information that must be provided, it is important that it flows and is appealing. Photos can be accessed from http://kemapics.brightfolio.net/apps/photos/album?albumid=52930417 or from your own source
Important that the final design fits printers template.(Flyers-A4-210x297mm-2Side - attached)

```html
<!DOCTYPE html>
<html lang="en">
<head>
<meta charset="utf-8">
<title>Blue Current Pools – 2014/15 Term Dates &amp; Prices</title>
<link href="https://fonts.googleapis.com/css2?family=Architects+Daughter&family=Arimo:ital,wght@0,400;0,700;1,400&family=Roboto+Condensed:wght@700&display=swap" rel="stylesheet">
<style>
:root{
  --sky:#29abe2;
  --panel:#1fb0e3;
  --panel-deep:#0f95cc;
  --head-cell:#5ccbec;
  --orange:#f7941d;
  --lime:#bfd130;
  --ink:#1a1a1a;
  --navy:#1b3a5c;
  --white:#ffffff;
  --star:#8dc63f;
  --hand:"Architects Daughter",cursive;
  --sans:"Arimo",Arial,sans-serif;
}
*{box-sizing:border-box;margin:0;padding:0}
html,body{width:849px;height:1200px;overflow:hidden;background:var(--white)}
.flyer{position:relative;width:849px;height:1200px;overflow:hidden;background:var(--white);font-family:var(--sans);color:var(--ink)}
.abs{position:absolute}

.hero-photo{left:0;top:0;width:849px;height:345px;background:linear-gradient(180deg,#9fd6ee 0%,#7cc6e8 55%,#b9e3f4 100%)}
.hero-edge{left:0;top:230px;width:849px;height:140px}

.title-bubble{left:36px;top:12px;width:165px;height:140px}
.title-bubble-text{left:40px;top:22px;width:152px;text-align:center;font-family:var(--hand);color:var(--white);font-size:21px;line-height:27px}
.term-subtitle{left:32px;top:154px;font-family:var(--hand);font-size:16px;color:var(--ink)}

.phone-pill{left:17px;top:219px;width:204px;height:63px;border-radius:32px;background:var(--orange);border:3px solid var(--white);box-shadow:0 0 0 2px var(--sky)}
.phone-label{left:38px;top:221px;font-size:12px;color:var(--white)}
.phone-number{left:38px;top:230px;font-family:"Roboto Condensed",Arial Narrow,sans-serif;font-size:40px;color:var(--white);letter-spacing:0.5px}
.website{left:19px;top:302px;font-size:16px;color:#2a5d8f}

.brand-box{left:649px;top:19px;width:174px;height:94px;background:var(--white);border-radius:12px;display:flex;align-items:center;justify-content:center;gap:8px}
.brand-dot{width:14px;height:14px;border-radius:50%;background:var(--orange)}
.brand-name{font-family:var(--sans);font-weight:700;font-size:17px;color:var(--sky);line-height:19px}

.important-title{left:632px;top:250px;font-family:var(--hand);font-size:26px;color:var(--orange)}
.important-list{left:533px;top:283px;width:300px;list-style:none}
.important-list li{position:relative;padding-left:14px;font-size:13px;font-weight:700;color:var(--sky);line-height:17px;margin-bottom:9px}
.important-list li::before{content:"★";position:absolute;left:0;top:0;font-size:10px;color:var(--star)}
.cap-note{left:504px;top:597px;width:330px;font-family:var(--hand);font-size:13.5px;line-height:17px;color:var(--ink)}

.pathway-title{left:19px;top:344px;font-family:var(--hand);font-size:27px;color:var(--sky)}
.pathway{left:19px;top:386px;width:290px}
.pathway .step{font-family:var(--hand);font-size:22px;color:var(--orange);line-height:28px}
.pathway .length{font-size:19px;font-weight:700;line-height:24px;margin-bottom:12px}

.baby-photo{left:304px;top:391px;width:190px;height:266px;border:3px solid var(--orange);border-radius:10px;background:linear-gradient(160deg,#cfeaf6 0%,#8fcfea 60%,#5fb5dc 100%)}

.footer-band{left:0;top:1100px;width:849px;height:100px;background:linear-gradient(90deg,#f7941d 0%,#bfd130 35%,#29abe2 65%,#f7941d 100%)}
.price-panel{left:17px;top:664px;width:815px;height:507px;background:var(--panel);border-radius:10px}
.panel-frame{left:28px;top:673px;width:798px;height:496px;border:2px dotted var(--white);border-radius:8px}
.panel-divider{left:425px;top:686px;width:0;height:222px;border-left:1px solid rgba(255,255,255,.45)}

.term-banner{width:330px;height:68px;background:var(--lime);font-family:var(--hand);font-size:21px;line-height:26px;color:#3a3a1a;text-align:center;padding-top:8px}
.term-banner.left{clip-path:polygon(0 0,100% 0,94% 100%,0 100%)}
.term-banner.right{clip-path:polygon(0 0,100% 0,100% 100%,6% 100%)}
.booking-note{width:357px;text-align:center;font-size:16px;color:var(--white)}
.price-table{width:357px;border-collapse:collapse;border:1px solid rgba(255,255,255,.8)}
.price-table th,.price-table td{width:25%;height:35px;border:1px solid rgba(255,255,255,.8);text-align:left;padding-left:9px;color:var(--white);font-weight:700}
.price-table th{background:var(--head-cell);font-size:17px}
.price-table th.small{font-size:13px}
.price-table td{font-size:17px;background:var(--panel)}
.holiday-note{left:28px;top:1136px;width:798px;text-align:center;font-style:italic;font-size:16px;color:var(--navy)}
</style>
</head>
<body>
<div class="flyer">
  <div class="abs hero-photo" role="img" aria-label="Photo of a smiling child in goggles swimming underwater"></div>
  <svg class="abs hero-edge" viewBox="0 0 849 140" preserveAspectRatio="none" aria-hidden="true">
    <path d="M0 70 C120 95 250 110 330 118 C380 104 420 92 480 90 C500 40 560 25 600 40 C640 5 720 5 760 30 C800 20 830 28 849 40 L849 140 L0 140 Z" fill="#ffffff"/>
  </svg>

  <svg class="abs title-bubble" viewBox="0 0 165 140" aria-hidden="true">
    <path d="M80 4 C130 4 162 30 162 66 C162 100 132 122 90 124 C70 126 55 134 40 139 C48 128 50 120 42 116 C14 104 2 86 2 64 C2 30 34 4 80 4 Z" fill="#1e9fd9"/>
  </svg>
  <div class="abs title-bubble-text">Blue Current<br>Pools<br>Classes</div>
  <div class="abs term-subtitle">2014/15 Term Dates &amp; Prices</div>

  <div class="abs phone-pill"></div>
  <div class="abs phone-label">Call us:</div>
  <div class="abs phone-number">9000 4821</div>
  <div class="abs website">www.bluecurrentpools.com.au</div>

  <div class="abs brand-box">
    <span class="brand-dot"></span>
    <span class="brand-name">blue current<br>pools</span>
  </div>

  <div class="abs important-title">Important</div>
  <ul class="abs important-list">
    <li>No bookings are taken without a fully completed enrolment form and payment.</li>
    <li>Read BCP Policies and Procedures for information on discounts, payment methods, refunds and makeups.</li>
    <li>Book early – places are limited due to small class sizes.</li>
    <li>Bookings can only be made in person at our Riverside Office or online.</li>
    <li>During holidays, all bookings must be done via the Riverside Office.</li>
    <li>Photographs and video footage is not allowed to be taken without the permission of all the parents / guardians whose children are in the class.</li>
  </ul>
  <div class="abs cap-note">All swimmers, male and female, are required to wear a cap – please name your cap and goggles with a biro to prevent it washing off.</div>

  <div class="abs pathway-title">Our Streamlined Pathway to Success</div>
  <div class="abs pathway">
    <div class="step">Baby Awareness</div>
    <div class="length">½ hour class per week</div>
    <div class="step">Baby Transition Classes</div>
    <div class="length">½ hour class per week</div>
    <div class="step">Blue Current Pools Classes</div>
    <div class="length">½ hour class per week</div>
    <div class="step">Transitional Stroke Group</div>
    <div class="length">1 hour class per week</div>
  </div>
  <div class="abs baby-photo" role="img" aria-label="Photo of a baby held by an instructor underwater"></div>

  <div class="abs footer-band" role="img" aria-label="Decorative orange and green wave pattern"></div>
  <div class="abs price-panel"></div>
  <div class="abs panel-frame"></div>
  <div class="abs panel-divider"></div>

  <div class="abs term-banner left" style="left:9px;top:703px">* 2014: Term 4 – 10 week term<br>Oct 6th – Dec 14th</div>
  <div class="abs booking-note" style="left:39px;top:779px">Bookings taken from 22nd Sep 2014</div>
  <table class="abs price-table" style="left:39px;top:806px">
    <tr><th>Babies</th><th class="small">Transition</th><th>BCP</th><th>TSG</th></tr>
    <tr><td>$155</td><td>$165</td><td>$170</td><td>$210</td></tr>
  </table>

  <div class="abs term-banner right" style="left:512px;top:703px">* 2015: Term 2 – 11 week term<br>Apr 13th – Jun 28th</div>
  <div class="abs booking-note" style="left:455px;top:779px">Bookings taken from 30th Mar 2015</div>
  <table class="abs price-table" style="left:455px;top:806px">
    <tr><th>Babies</th><th class="small">Transition</th><th>BCP</th><th>TSG</th></tr>
    <tr><td>$170.5</td><td>$176</td><td>$181.5</td><td>$231</td></tr>
  </table>

  <div class="abs term-banner left" style="left:9px;top:941px">* 2015: Term 1 – 9 week term<br>Jan 27th – Mar 29th</div>
  <div class="abs booking-note" style="left:39px;top:1018px">Bookings taken from 15th Dec 2014</div>
  <table class="abs price-table" style="left:39px;top:1045px">
    <tr><th>Babies</th><th class="small">Transition</th><th>BCP</th><th>TSG</th></tr>
    <tr><td>$139.50</td><td>$148.5</td><td>$153</td><td>$189</td></tr>
  </table>

  <div class="abs term-banner right" style="left:512px;top:941px">2015: Term 3 – 10 week term<br>Jul 13th – Sep 20th</div>
  <div class="abs booking-note" style="left:455px;top:1018px">Bookings taken from 29th Jun 2015</div>
  <table class="abs price-table" style="left:455px;top:1045px">
    <tr><th>Babies</th><th class="small">Transition</th><th>BCP</th><th>TSG</th></tr>
    <tr><td>$160</td><td>$170</td><td>$175</td><td>$215</td></tr>
  </table>

  <div class="abs holiday-note">* Note that these terms have public holidays and prices will be adjusted accordingly.</div>
</div>
</body>
</html>
```